New counselling and hypnotherapy business

I'd like a flyer which is relevant to people who want support and to improve their wellbeing which follows the same theme as my website: http://wrenlowtherapy.sitepailo.com
And emphasise that whatever the area of concern, development or growth and I can tailor my knowledge and skills to help.

I'd like to use the same logo and my emphasis is to draw the audience in...therapy and counselling is for people who are "stuck" and having a difficult time...it can also be useful has a personal development tool.

Hypnotherapy

```html
<!DOCTYPE html>
<html lang="en">
<head>
<meta charset="utf-8">
<title>Wrenlow Counselling &amp; Hypnotherapy – Flyer</title>
<link rel="stylesheet" href="https://fonts.googleapis.com/css2?family=EB+Garamond:wght@500;700;800&display=swap">
<style>
  :root {
    --paper: #ffffff;
    --violet-deep: #8a3de2;
    --violet-soft: #c9a6f2;
    --headline-green: #4cf000;
    --headline-shadow: rgba(60, 50, 70, 0.55);
    --ink: #111111;
    --brand-violet: #7f3fcf;
  }
  * { margin: 0; padding: 0; box-sizing: border-box; }
  html, body {
    width: 857px;
    height: 1200px;
    overflow: hidden;
    background: var(--paper);
  }
  .flyer {
    position: relative;
    width: 857px;
    height: 1200px;
    background: var(--paper);
    font-family: "EB Garamond", Garamond, serif;
    color: var(--ink);
  }
  .hero {
    position: absolute;
    left: 55px;
    top: 52px;
    width: 750px;
    height: 465px;
    overflow: hidden;
    background: linear-gradient(to bottom, var(--violet-deep) 0%, var(--violet-soft) 45%, #ece0fb 80%, var(--paper) 100%);
  }
  .headline {
    position: absolute;
    font-weight: 800;
    color: var(--headline-green);
    line-height: 1;
    white-space: nowrap;
    text-shadow: 9px 9px 7px var(--headline-shadow);
    letter-spacing: -1px;
  }
  .headline--talk  { left: 38px;  top: 22px;  font-size: 126px; }
  .headline--heard { left: 150px; top: 146px; font-size: 120px; }
  .headline--you   { left: 85px;  top: 249px; font-size: 185px; letter-spacing: -4px; }

  .pitch {
    position: absolute;
    left: 30px;
    top: 536px;
    width: 797px;
    text-align: center;
    font-weight: 700;
    font-size: 35.5px;
    line-height: 51px;
  }

  .brand {
    position: absolute;
    left: 62px;
    top: 990px;
    width: 330px;
    color: var(--brand-violet);
    font-weight: 500;
    font-size: 38px;
    line-height: 40px;
    letter-spacing: 1px;
  }
  .brand__mark {
    display: block;
    width: 26px;
    height: 26px;
    border-radius: 50%;
    background: var(--brand-violet);
    margin-bottom: 12px;
  }

  .contact {
    position: absolute;
    left: 420px;
    top: 925px;
    width: 410px;
    text-align: center;
    font-style: normal;
    font-weight: 700;
    font-size: 25px;
    line-height: 29px;
  }
  .contact__address { margin-bottom: 22px; }
  .contact__phone   { margin-bottom: 22px; }
</style>
</head>
<body>
<main class="flyer">
  <section class="hero">
    <div class="headline headline--talk">Talk…</div>
    <div class="headline headline--heard">Be Heard…</div>
    <div class="headline headline--you">Be YOU</div>
  </section>

  <p class="pitch">
    Whatever the area of concern,<br>
    development or growth, I tailor my<br>
    knowledge and training to help those who are<br>
    feeling “stuck” and having a difficult time<br>
    in a safe, confidential environment.
  </p>

  <div class="brand">
    <span class="brand__mark"></span>
    Wrenlow<br>Counselling &amp;<br>Hypnotherapy
  </div>

  <address class="contact">
    <p class="contact__address">12B, Harbour Lane,<br>Saltmere<br>East Sussex BN7 4QX</p>
    <p class="contact__phone">Tel. 07700 900418</p>
    <p class="contact__web">wrenlowtherapy@mailhollow.com<br>wrenlowtherapy.sitepailo.com</p>
  </address>
</main>
</body>
</html>
```